Media and Film Company Needs a New Website

We produce highly stylized commercials and film pieces for our clients. We also produce live events, both corporate and theatrical. Looking for a site that can show off our client videos - have a polished way to show off our team, and be able to create pages to highlight our clients and give a full overview of our project/process with them. We design simple website for some of our clients - so we are very wordpress familiar, and would like something that doesn't feel like a template.

Target Market(s)

content creators, creative directors, production teams, marketing agencies

Industry/Entity Type

Film Production

Number of Pages Required

4 page

Font styles to use
Sans Serif

Requirements
Must have
• slick looking video embed (from YT or Vimeo)
• project pages - client snapshot (what we did for them, how we did it)
• nice landing page, have our company video reel on the page
• testimonials
• contact page
• ability to have photos as a background if we want
Nice to have
• polished clean look - look to our logo colors and linear elements
• we produce very stylized videos for our clients and our website should reflect that
Should not have
• template look or feel to it- please bring your flare to the project!
• take a look at our current site - zantorvo.com we need a better way to highlight our work and our clients

```html
<!DOCTYPE html>
<html lang="en">
<head>
<meta charset="utf-8">
<title>Zantorvo Media &amp; Entertainment</title>
<link href="https://fonts.googleapis.com/css2?family=Abril+Fatface&family=Montserrat:wght@400;500;600&display=swap" rel="stylesheet">
<style>
:root{
  --ink:#1d1d1d;
  --night:#0f0f12;
  --white:#ffffff;
  --gold:#c9a227;
  --gold-soft:#d8b548;
  --muted:#555555;
  --line:#8a8a8a;
  --panel-shadow:rgba(0,0,0,.18);
}
*{box-sizing:border-box;margin:0;padding:0}
html,body{width:1200px;height:2761px;overflow:hidden}
body{position:relative;background:var(--white);font-family:"Montserrat",sans-serif;color:var(--ink)}
.abs{position:absolute}

/* hero */
.hero{left:0;top:0;width:1200px;height:662px;
  background:radial-gradient(ellipse at 60% 40%,#3a3630 0%,#1d1b19 45%,#0b0b0d 100%)}
.brand{left:77px;top:40px;color:var(--white);font-weight:600;font-size:24px;letter-spacing:2px;display:flex;align-items:center;gap:10px}
.brand .dot{width:12px;height:12px;background:var(--white);display:inline-block}
.nav{right:208px;top:52px;display:flex;gap:30px;font-size:10px;letter-spacing:.3px;color:var(--white);text-transform:uppercase;white-space:nowrap}
.social{display:flex;gap:14px}
.social span{width:13px;height:13px;border-radius:50%;background:var(--white);display:block}
.social.top{left:1030px;top:50px}
.hero-title{left:480px;top:316px;width:640px;text-align:center;color:var(--white);font-family:"Abril Fatface",serif;font-weight:400;font-size:32px;line-height:36px;white-space:nowrap}
.btn-outline{border:2px solid var(--white);border-radius:20px;color:var(--white);font-size:15px;text-align:center;line-height:36px}
.hero-btn{left:725px;top:410px;width:135px;height:40px}
.dots{left:777px;top:473px;display:flex;gap:3px}
.dots span{width:7px;height:7px;border:1.5px solid var(--white);border-radius:50%}
.arrow{top:330px;width:20px;height:24px}

/* panel */
.panel{left:147px;top:565px;width:904px;height:1613px;background:var(--white);box-shadow:0 0 18px var(--panel-shadow)}
.h-serif{font-family:"Abril Fatface",serif;font-weight:400;text-align:center;text-transform:uppercase}
.about-title{left:147px;top:610px;width:904px;font-size:21px;color:var(--ink)}
.about-copy{left:210px;top:660px;width:780px;font-size:10.5px;line-height:15px;color:var(--muted);text-align:center}
.about-copy p{margin-bottom:13px}

.reel{left:254px;top:820px;width:684px;height:376px;background:#1f1f1f;border:2px solid #444}
.reel-brand{left:0;top:118px;width:684px;text-align:center;color:var(--white);font-weight:600;font-size:32px;letter-spacing:1px;white-space:nowrap}
.reel-title{left:0;top:220px;width:684px;text-align:center;color:#e8e8e8;font-weight:400;font-size:60px;line-height:70px;letter-spacing:1px;white-space:nowrap}
.reel-bar{left:0;top:336px;width:684px;height:38px}

.thumb{top:1221px;width:185px;height:104px}
.thumb-arrow{top:1256px;width:26px;height:26px;border:1.5px solid var(--gold);color:var(--gold)}
.link-badge{width:34px;height:34px;border-radius:50%;background:rgba(255,255,255,.75);left:50%;top:50%;transform:translate(-50%,-50%)}

.featured-title{left:147px;top:1368px;width:904px;font-size:21px;color:var(--gold)}
.photo{top:1436px;width:279px;height:182px}

.portfolio-btn{left:530px;top:1662px;width:136px;height:36px;border:2px solid var(--gold);border-radius:18px;font-size:10px;text-align:center;line-height:32px;text-transform:uppercase}
.what-title{left:147px;top:1712px;width:904px;font-size:21px;color:var(--ink)}
.card{top:1776px;width:199px;height:300px;background:var(--white);box-shadow:0 2px 8px rgba(0,0,0,.22)}
.card .shot{position:absolute;left:0;top:0;width:199px;height:132px}
.card ul{position:absolute;left:0;top:166px;width:199px;list-style:none;text-align:center;font-size:10px;line-height:13px;text-transform:uppercase;color:var(--ink)}
.card li{margin-bottom:13px}

/* footer */
.footer{left:0;top:2144px;width:1200px;height:617px;background:linear-gradient(180deg,#242424 0%,#1a1a1a 50%,#2b2b2b 100%)}
.contact-title{left:0;top:2242px;width:1200px;font-size:21px;color:var(--white)}
.field{height:26px;border-bottom:1px solid var(--line);color:#d0d0d0;font-size:11px}
.send{left:546px;top:2530px;width:104px;height:30px;border:2px solid var(--white);color:var(--white);font-family:"Abril Fatface",serif;font-size:13px;text-align:center;line-height:26px;letter-spacing:1px}
.foot-brand{left:0;top:2610px;width:1200px;text-align:center;color:var(--white);font-weight:600;font-size:24px;letter-spacing:2px}
.copyright{left:77px;top:2715px;font-size:10px;color:#cfcfcf}
.social.bottom{left:1040px;top:2714px}
</style>
</head>
<body>

<div class="abs hero" role="img" aria-label="Dark cinematic photo of a vintage film projector and a clapperboard"></div>
<div class="abs brand"><span class="dot"></span>ZANTORVO</div>
<nav class="abs nav"><span>Home</span><span>Portfolio</span><span>About Zantorvo</span><span>Testimonials</span><span>Press</span><span>Contact</span></nav>
<div class="abs social top"><span></span><span></span><span></span></div>
<svg class="abs arrow" style="left:58px" viewBox="0 0 20 24"><path d="M14 4 L6 12 L14 20" fill="none" stroke="#fff" stroke-width="3"/></svg>
<svg class="abs arrow" style="left:1132px" viewBox="0 0 20 24"><path d="M6 4 L14 12 L6 20" fill="none" stroke="#fff" stroke-width="3"/></svg>
<h1 class="abs hero-title">Welcome to<br>Zantorvo Media &amp; Entertainment</h1>
<div class="abs btn-outline hero-btn">LEARN MORE</div>
<div class="abs dots"><span></span><span></span><span></span><span></span></div>

<section class="abs panel"></section>
<h2 class="abs h-serif about-title">About Zantorvo Media &amp; Entertainment</h2>
<div class="abs about-copy">
  <p>Zantorvo Media &amp; Entertainment provides full-service campaigns in film and media production, live entertainment &amp; theatrical production, marketing &amp; advertising, and event management in the DC metro area.</p>
  <p>Founded in 2009, Zantorvo Media &amp; Entertainment has built a reputation working for clients including the Northgate Screen Institute, Larkfield Leaders Forum, Brennick Music, Riverbend Community Partners, and Calloway Events.</p>
  <p>Zantorvo Media &amp; Entertainment works to build strong relationships with its clients through full-service campaigns in multiple industries. Through community outreach, Zantorvo develops its campaigns thoroughly to provide the most successful services to its clients.</p>
</div>

<div class="abs reel">
  <div class="abs reel-brand">ZANTORVO MEDIA &amp; ENTERTAINMENT</div>
  <div class="abs reel-title">2015 Demo Reel</div>
  <svg class="abs reel-bar" viewBox="0 0 684 38">
    <path d="M22 12 L22 26 L33 19 Z" fill="#fff"/>
    <rect x="60" y="18" width="470" height="3" fill="#555"/>
    <rect x="60" y="18" width="10" height="3" fill="#9ad"/>
    <rect x="545" y="13" width="3" height="12" fill="#ccc"/><rect x="551" y="11" width="3" height="14" fill="#ccc"/><rect x="557" y="9" width="3" height="16" fill="#ccc"/>
    <text x="590" y="24" fill="#fff" font-family="Montserrat,sans-serif" font-size="11" font-weight="600">HD</text>
    <rect x="620" y="13" width="10" height="10" fill="none" stroke="#ccc" stroke-width="1.5"/>
    <rect x="642" y="13" width="10" height="10" fill="none" stroke="#ccc" stroke-width="1.5"/>
  </svg>
</div>

<svg class="abs thumb-arrow" style="left:163px" viewBox="0 0 26 26"><path d="M15 8 L10 13 L15 18" fill="none" stroke="#c9a227" stroke-width="2"/></svg>
<div class="abs thumb" style="left:199px;background:linear-gradient(135deg,#2d4a6a,#9fb2c4)" role="img" aria-label="Event venue exterior thumbnail"><span class="abs link-badge"></span></div>
<div class="abs thumb" style="left:403px;background:linear-gradient(135deg,#c7a36a,#e6ddd0)" role="img" aria-label="Community event thumbnail"><span class="abs link-badge"></span></div>
<div class="abs thumb" style="left:609px;background:linear-gradient(180deg,#8fb0d0,#6d8a4a)" role="img" aria-label="Building exterior thumbnail"><span class="abs link-badge"></span></div>
<div class="abs thumb" style="left:814px;background:linear-gradient(135deg,#1e3a8a,#4a6fd0)" role="img" aria-label="Speaker on stage thumbnail"><span class="abs link-badge"></span></div>
<svg class="abs thumb-arrow" style="left:1010px" viewBox="0 0 26 26"><path d="M11 8 L16 13 L11 18" fill="none" stroke="#c9a227" stroke-width="2"/></svg>

<h2 class="abs h-serif featured-title">Featured Photos</h2>
<div class="abs photo" style="left:158px;background:linear-gradient(180deg,#3a2a2a,#6a2a1a 60%,#2a1a14)" role="img" aria-label="Audience in a theater at a documentary festival"><span class="abs link-badge"></span></div>
<div class="abs photo" style="left:458px;background:linear-gradient(135deg,#2a3e7a,#5a7ac0 60%,#2a2a3a)" role="img" aria-label="Speaker at a podium at a public event"><span class="abs link-badge"></span></div>
<div class="abs photo" style="left:759px;background:linear-gradient(135deg,#b8c0b0,#8a9a7a 60%,#c8b8a8)" role="img" aria-label="Audience members seated at a screening"><span class="abs link-badge"></span></div>

<div class="abs portfolio-btn">See our portfolio</div>
<h2 class="abs h-serif what-title">What We Do</h2>

<div class="abs card" style="left:180px">
  <div class="shot" style="background:linear-gradient(135deg,#5a4a2a,#c8b87a)" role="img" aria-label="Studio lighting and camera setup"></div>
  <ul><li>Pro Design Suite</li><li>Motion Graphics</li><li>4K Workflow</li><li>Direct to Web/Online</li></ul>
</div>
<div class="abs card" style="left:391px">
  <div class="shot" style="background:linear-gradient(135deg,#7a7a4a,#c8c89a)" role="img" aria-label="Production crew on set"></div>
  <ul><li>Theatrical Producing</li><li>Production Management</li><li>Lighting &amp; Video Design</li><li>Audio System Design</li></ul>
</div>
<div class="abs card" style="left:602px">
  <div class="shot" style="background:linear-gradient(135deg,#8a3a0a,#e8902a)" role="img" aria-label="Performers on a stage in warm light"></div>
  <ul><li>Branding</li><li>Social Media</li><li>Media Relations and<br>Outreach</li><li>Street Teams</li></ul>
</div>
<div class="abs card" style="left:815px">
  <div class="shot" style="background:linear-gradient(135deg,#6a4a1a,#e0a04a)" role="img" aria-label="Concert crowd with raised hands"></div>
  <ul><li>Event Production</li><li>Staffing &amp; Hiring</li><li>Manage RFPs</li><li>Sponsor Relations</li></ul>
</div>

<footer class="abs footer" role="img" aria-label="Black and white photo of a vintage film crew with cameras"></footer>
<h2 class="abs h-serif contact-title">Contact Us</h2>
<div class="abs field" style="left:221px;top:2300px;width:367px">Name</div>
<div class="abs field" style="left:610px;top:2300px;width:366px">Email</div>
<div class="abs field" style="left:221px;top:2351px;width:367px">Phone</div>
<div class="abs field" style="left:610px;top:2351px;width:366px">Subjects</div>
<div class="abs field" style="left:221px;top:2402px;width:755px;height:101px">Mesage</div>
<div class="abs send">SEND</div>
<div class="abs foot-brand">ZANTORVO</div>
<div class="abs copyright">© 2016 zantorvo media entertainment &nbsp;| &nbsp;All Rights Reserved</div>
<div class="abs social bottom"><span></span><span></span><span></span></div>

</body>
</html>
```